Halvik builders

Tarven Q480 year 2021 needs a full wrap. My companies name is Halvik Builders we are a high end landscape design build company. We specialize in pavers retaining walls, patio covers and decks.

```html
<!DOCTYPE html>
<html lang="en">
<head>
<meta charset="utf-8">
<title>Halvik Builders – Tarven Q480 Wrap</title>
<link rel="stylesheet" href="https://fonts.googleapis.com/css2?family=Poppins:wght@600&family=Roboto+Condensed:wght@500&display=swap">
<style>
  :root {
    --teal: #1b6484;
    --teal-dark: #14506b;
    --white: #ffffff;
    --silver: #d9dde0;
    --glass: #6d7074;
    --tyre: #1c1c1c;
    --trim: #111111;
    --hub: #b9bcbf;
    --yellow: #f7c600;
    --ink: #1a1a1a;
    --tail: #7a1a1a;
    --bg: #ffffff;
  }
  html, body { margin: 0; padding: 0; overflow: hidden; background: var(--bg); }
  .canvas { position: relative; width: 1200px; height: 730px; overflow: hidden; background: var(--bg); }
  .wrap-art { position: absolute; inset: 0; }
  .company-name { font-family: "Poppins", sans-serif; font-weight: 600; fill: var(--white); }
  .tagline { font-family: "Poppins", sans-serif; font-weight: 600; fill: var(--silver); }
  .pill-text { font-family: "Roboto Condensed", sans-serif; font-weight: 500; fill: var(--ink); }
</style>
</head>
<body>
<div class="canvas">
  <svg class="wrap-art" width="1200" height="730" viewBox="0 0 1200 730" xmlns="http://www.w3.org/2000/svg">
    <defs>
      <clipPath id="body-clip">
        <path d="M128,330 Q140,312 300,292 L330,290 L430,224 Q450,214 520,212 L640,210 L652,222 L658,296 L1048,294 L1055,300 L1058,430 L945,432 A68,68 0 0 0 810,432 L305,432 A68,68 0 0 0 170,432 L130,430 Z"/>
      </clipPath>
    </defs>

    <!-- vehicle body panel -->
    <g class="vehicle-body">
      <path fill="var(--teal)" d="M128,330 Q140,312 300,292 L330,290 L430,224 Q450,214 520,212 L640,210 L652,222 L658,296 L1048,294 L1055,300 L1058,430 L945,432 A68,68 0 0 0 810,432 L305,432 A68,68 0 0 0 170,432 L130,430 Z"/>
      <path fill="var(--glass)" d="M352,308 L430,234 Q440,228 515,226 L515,305 Z"/>
      <rect x="552" y="225" width="63" height="68" rx="8" fill="var(--glass)"/>
      <line x1="532" y1="222" x2="532" y2="430" stroke="var(--teal-dark)" stroke-width="2"/>
      <line x1="643" y1="222" x2="650" y2="430" stroke="var(--teal-dark)" stroke-width="2"/>
      <line x1="340" y1="300" x2="345" y2="430" stroke="var(--teal-dark)" stroke-width="2"/>
      <rect x="486" y="320" width="34" height="10" rx="4" fill="var(--teal-dark)"/>
      <rect x="678" y="350" width="40" height="26" rx="5" fill="none" stroke="var(--teal-dark)" stroke-width="1.5"/>
      <rect x="1027" y="312" width="30" height="72" rx="4" fill="var(--tail)"/>
      <rect x="122" y="398" width="48" height="44" rx="4" fill="var(--trim)"/>
      <rect x="1040" y="384" width="34" height="34" rx="3" fill="var(--trim)"/>
      <rect x="132" y="333" width="14" height="60" rx="3" fill="var(--silver)"/>
    </g>

    <!-- material swatches -->
    <g class="material-swatches" clip-path="url(#body-clip)" stroke="var(--white)" stroke-width="4">
      <rect role="img" aria-label="Grey cobblestone paver texture" x="-46" y="-46" width="92" height="92" rx="8" fill="#9c9ea0" transform="translate(752,390) rotate(45)"/>
      <rect role="img" aria-label="Brown granite stone texture" x="-44" y="-44" width="88" height="88" rx="8" fill="#7b6b4f" transform="translate(830,342) rotate(30)"/>
      <rect role="img" aria-label="White marble texture" x="-34" y="-34" width="68" height="68" rx="8" fill="#e8e8e8" transform="translate(888,330) rotate(45)"/>
      <rect role="img" aria-label="Stacked brick wall texture" x="-40" y="-40" width="80" height="80" rx="8" fill="#7d5b49" transform="translate(950,345) rotate(28)"/>
      <rect role="img" aria-label="Sandstone slab texture" x="-38" y="-38" width="76" height="76" rx="8" fill="#d9ccb5" transform="translate(982,395) rotate(45)"/>
    </g>

    <!-- fender flare and wheels -->
    <path d="M800,432 A78,78 0 0 1 955,432 L945,432 A68,68 0 0 0 810,432 Z" fill="var(--tyre)"/>
    <g class="wheels">
      <circle cx="237" cy="450" r="60" fill="var(--tyre)"/>
      <circle cx="237" cy="450" r="36" fill="var(--hub)"/>
      <circle cx="877" cy="450" r="60" fill="var(--tyre)"/>
      <circle cx="877" cy="450" r="36" fill="var(--hub)"/>
    </g>

    <!-- front fender name -->
    <text class="company-name" x="172" y="342" font-size="13">Halvik Builders</text>

    <!-- door name -->
    <text class="company-name" x="352" y="358" font-size="24">Halvik Builders</text>
    <circle cx="608" cy="350" r="18" fill="var(--silver)"/>
    <text class="tagline" x="353" y="385" font-size="11">Outdoor Living Spaces</text>

    <!-- phone pill -->
    <rect x="343" y="397" width="135" height="20" rx="10" fill="var(--yellow)" stroke="var(--white)" stroke-width="1.5"/>
    <text class="pill-text" x="410" y="411.5" font-size="10.5" text-anchor="middle">Call Us Now! (555) 014-2280</text>

    <!-- web pill -->
    <rect x="655" y="311" width="116" height="16" rx="8" fill="var(--white)"/>
    <text class="pill-text" x="713" y="322.5" font-size="8.5" text-anchor="middle">www.halvikbuilders.com</text>
  </svg>
</div>
</body>
</html>
```